Stationery Design Project

Require letterhead/stationery design based on new logo (see attached).

Would prefer it kept simple but strong and effective.

Target Market(s)

Clients and building developers. Residential/consumer and corporate clientele.

```html
<!DOCTYPE html>
<html lang="en">
<head>
<meta charset="utf-8">
<title>Stonecrest Builders — Business Cards</title>
<link rel="stylesheet" href="https://fonts.googleapis.com/css2?family=Questrial&display=swap">
<style>
  :root {
    --backdrop: #2a2a2a;
    --card: #1b1b1c;
    --card-edge: #2c2c2e;
    --accent: #2fa8d8;
    --silver: #a9a9ab;
    --muted: #8a8a8c;
    --rule: #5a5a5c;
  }
  * { margin: 0; padding: 0; box-sizing: border-box; }
  html, body {
    width: 1200px;
    height: 900px;
    overflow: hidden;
    background: var(--backdrop);
    font-family: "Questrial", "Century Gothic", sans-serif;
  }
  .canvas {
    width: 1200px;
    height: 900px;
    display: flex;
    flex-direction: column;
    align-items: center;
    justify-content: center;
    gap: 50px;
  }
  .card {
    position: relative;
    width: 665px;
    height: 380px;
    background: var(--card);
    border: 1px solid var(--card-edge);
    box-shadow: 0 10px 30px rgba(0,0,0,0.45);
  }
  .brand {
    display: flex;
    align-items: center;
    gap: 14px;
    color: var(--silver);
    text-transform: uppercase;
    letter-spacing: 0.08em;
  }
  .brand-mark {
    background: var(--accent);
    flex: none;
  }
  /* Front */
  .card--front .brand {
    position: absolute;
    inset: 0;
    justify-content: center;
    font-size: 34px;
  }
  .card--front .brand-mark { width: 30px; height: 30px; }
  /* Back */
  .card--back .brand {
    position: absolute;
    left: 52px;
    top: 128px;
    font-size: 24px;
  }
  .card--back .brand-mark { width: 22px; height: 22px; }
  .holder {
    position: absolute;
    right: 44px;
    top: 112px;
    text-align: right;
  }
  .holder-name {
    color: var(--accent);
    font-size: 22px;
    font-weight: 700;
    letter-spacing: 0.04em;
    text-transform: uppercase;
  }
  .holder-role {
    color: var(--silver);
    font-size: 14px;
    margin-top: 4px;
  }
  .contact {
    position: absolute;
    right: 44px;
    top: 206px;
    text-align: right;
    color: var(--muted);
    font-size: 12.5px;
    line-height: 1.6;
    letter-spacing: 0.02em;
  }
  .contact-label { color: var(--accent); }
  .rule {
    position: absolute;
    left: 96px;
    right: 44px;
    bottom: 70px;
    height: 1px;
    background: var(--rule);
  }
</style>
</head>
<body>
  <main class="canvas">
    <section class="card card--front" aria-label="Business card front">
      <div class="brand">
        <span class="brand-mark"></span>
        <span class="brand-name">Stonecrest Builders</span>
      </div>
    </section>

    <section class="card card--back" aria-label="Business card back">
      <div class="brand">
        <span class="brand-mark"></span>
        <span class="brand-name">Stonecrest Builders</span>
      </div>
      <div class="holder">
        <p class="holder-name">Karan Mehra</p>
        <p class="holder-role">Managing Director</p>
      </div>
      <address class="contact" style="font-style:normal">
        12/3, Near Harbour Road, Devka, Nani Daman<br>
        U.T. OF DAMAN - 396555 · <span class="contact-label">Tel:</span> +91 260 555 0142
      </address>
      <div class="rule"></div>
    </section>
  </main>
</body>
</html>
```